Plastering (solid plastering) business card design

We need a business card for a a small plastering business based in Perth Western Australia. We are a small team that provides a service in solid plastering specialising in float, white set and sand finish. We would like to see a clean business card with our name "Ridgeline Render Co" being the focus of the card and maybe incorporated into a logo. We don't have a logo at the moment so we would like to see some cards that may provide us with our future logo.

Industry/Entity Type

Business

Contact Information for Business Card

Ridgeline Render Co

Solid Plastering Specialists

Ph: Corey 0418730615
Ph: Luke 0451082963

Requirements
Should not have
• The design should not have Drywall incorporated into the card. In perth W.A. Plastering in different to someone that puts up Panelmax. We use sand, cement, lime and hardwall plaster.

```html
<!DOCTYPE html>
<html lang="en">
<head>
<meta charset="utf-8">
<title>Ridgeline Render Co – Business Card</title>
<link rel="stylesheet" href="https://fonts.googleapis.com/css2?family=Mulish:wght@600;800&family=Michroma&display=swap">
<style>
  :root {
    --backdrop: #e9e7e4;
    --card-white: #ffffff;
    --ink: #111111;
    --orange: #f08a1c;
    --orange-deep: #e4621f;
    --band-black: #0c0c0c;
    --band-text: #f2f2f2;
  }
  * { margin: 0; padding: 0; box-sizing: border-box; }
  html, body {
    width: 1200px;
    height: 800px;
    overflow: hidden;
    background: var(--backdrop);
  }
  .canvas {
    position: relative;
    width: 1200px;
    height: 800px;
    display: flex;
    align-items: center;
    justify-content: center;
  }
  .business-card {
    position: relative;
    width: 900px;
    height: 514px;
    background: var(--card-white);
    box-shadow: 0 18px 40px rgba(0,0,0,0.18);
    overflow: hidden;
    font-family: "Mulish", Arial, sans-serif;
  }
  .brand {
    position: absolute;
    left: 64px;
    top: 78px;
    display: flex;
    align-items: center;
    gap: 26px;
  }
  .brand-dot {
    width: 120px;
    height: 120px;
    border-radius: 50%;
    background: var(--orange);
    flex: none;
  }
  .brand-name {
    font-weight: 800;
    font-size: 56px;
    line-height: 0.98;
    color: var(--ink);
    letter-spacing: -0.5px;
  }
  .contacts {
    position: absolute;
    left: 64px;
    top: 300px;
    display: grid;
    grid-template-columns: auto auto;
    column-gap: 10px;
    row-gap: 2px;
    align-items: baseline;
  }
  .contact-name {
    font-weight: 600;
    font-size: 34px;
    color: var(--orange);
  }
  .contact-number {
    font-weight: 600;
    font-size: 40px;
    color: var(--ink);
    letter-spacing: 0.5px;
  }
  .tagline-band {
    position: absolute;
    left: 0;
    right: 0;
    bottom: 0;
    height: 62px;
    background: var(--band-black);
    border-top: 5px solid var(--orange);
    border-image: linear-gradient(90deg, var(--orange-deep), var(--orange)) 1;
    display: flex;
    align-items: center;
    justify-content: center;
  }
  .tagline {
    font-family: "Michroma", "Arial Black", sans-serif;
    font-size: 20px;
    font-variant: small-caps;
    letter-spacing: 12px;
    color: var(--band-text);
    white-space: nowrap;
  }
</style>
</head>
<body>
  <main class="canvas">
    <article class="business-card">
      <header class="brand">
        <span class="brand-dot" aria-hidden="true"></span>
        <h1 class="brand-name">Ridgeline<br>Render Co</h1>
      </header>

      <dl class="contacts">
        <dt class="contact-name">Corey :</dt>
        <dd class="contact-number">0418730615</dd>
        <dt class="contact-name">Luke :</dt>
        <dd class="contact-number">0451082963</dd>
      </dl>

      <footer class="tagline-band">
        <p class="tagline">Solid Plastering Specialists</p>
      </footer>
    </article>
  </main>
</body>
</html>
```